Verdant Bayline post card / handouts for customers

I am a New Orleans based meal prep company for health and fitness minded people who delivers executive chef quality food right to your door weekly. I am seeking a handout / postcard sized brochure that is straight and to the point. I need it to state step 1) go online step 2) order a la carte menu 3) deliver.

I will get into further detail with whomever I work with on specs.

My aesthetic is MODERN. I like LUMEVI.example aesthetic. Clean is key, Postcard design is 2 sided.

Industry/Entity Type

Fitness

Requirements
Must have
• Clean modern lines and photos. Bright and white!
Should not have
• Too busy, cluttered, too much info.

```html
<!DOCTYPE html>
<html lang="en">
<head>
<meta charset="utf-8">
<title>Verdant Bayline Postcard</title>
<link rel="stylesheet" href="https://fonts.googleapis.com/css2?family=Josefin+Sans:wght@300&family=Oswald:wght@400&family=Open+Sans:wght@400&display=swap">
<style>
  :root {
    --page: #ecebe8;
    --card: #ffffff;
    --ink: #2b2b2d;
    --body: #555557;
    --gold: #a8895e;
    --bar: #3a3a3c;
    --bar-text: #ffffff;
  }
  * { box-sizing: border-box; margin: 0; padding: 0; }
  html, body { width: 1192px; height: 1200px; overflow: hidden; background: var(--page); }
  .canvas { position: relative; width: 1192px; height: 1200px; }
  .card {
    position: absolute; width: 800px; height: 518px; background: var(--card);
    box-shadow: 0 4px 14px rgba(0,0,0,.18); overflow: hidden;
  }
  .card--front { left: 172px; top: 57px; }
  .card--back { left: 250px; top: 625px; }

  .photo { position: absolute; }
  .photo--salmon { left: 0; top: 0; width: 445px; height: 322px;
    background: radial-gradient(circle at 55% 50%, #f4f1ec 0 38%, transparent 39%),
                radial-gradient(circle at 55% 50%, #5f8a3a 0 30%, transparent 60%),
                linear-gradient(135deg, #e9e6e0, #d8d5cf); }
  .photo--lobster { left: 0; top: 333px; width: 145px; height: 145px;
    background: linear-gradient(135deg, #e8d3b6, #c46b3e 55%, #6e4a34); }
  .photo--greens { left: 150px; top: 333px; width: 145px; height: 145px;
    background: linear-gradient(135deg, #f1f1ee, #cfd9bf 50%, #5d7f3a); }
  .photo--tacos { left: 300px; top: 333px; width: 145px; height: 145px;
    background: linear-gradient(135deg, #d9c3a0, #8a5a3a 55%, #e5dfd6); }
  .photo--bowl { left: 0; top: 203px; width: 800px; height: 155px;
    background: linear-gradient(90deg, #6f9a45 0%, #c9a070 30%, #d8574a 45%, #9fb37a 62%, #eeeeec 75%, #f4f4f2 100%); }

  .brand { position: absolute; display: flex; flex-direction: column; align-items: center; text-align: center; }
  .brand__dot { width: 64px; height: 64px; border: 2px solid var(--ink); border-radius: 50%; }
  .brand__name {
    font-family: "Josefin Sans", sans-serif; font-weight: 300; color: var(--ink);
    text-transform: uppercase; white-space: nowrap; letter-spacing: 1px;
  }
  .tagline { font-family: "Oswald", sans-serif; color: var(--gold); text-transform: uppercase; letter-spacing: .3px; }

  .front-brand { left: 445px; width: 355px; top: 50px; }
  .front-brand .brand__name { font-size: 33px; margin-top: 22px; }
  .front-brand .tagline { font-size: 21px; margin-top: 14px; }

  .promise {
    position: absolute; left: 460px; top: 229px; width: 326px; height: 55px;
    background: var(--bar); color: var(--bar-text);
    font-family: "Open Sans", sans-serif; font-size: 15.5px; line-height: 21px;
    display: flex; align-items: center; justify-content: center; text-align: center;
  }
  .steps { position: absolute; left: 468px; top: 304px; list-style: none; }
  .step { display: flex; align-items: center; height: 42px; margin-bottom: 12px; }
  .step__num {
    width: 42px; height: 42px; border: 2px solid var(--gold); border-radius: 50%;
    display: flex; align-items: center; justify-content: center;
    font-family: "Open Sans", sans-serif; font-size: 16px; color: var(--ink); flex: none;
  }
  .step__text { margin-left: 14px; font-family: "Open Sans", sans-serif; font-size: 16px; line-height: 20px; color: var(--ink); }

  .back-brand { left: 0; width: 800px; top: 22px; }
  .back-brand .brand__dot { width: 56px; height: 56px; }
  .back-brand .brand__name { font-size: 30px; margin-top: 18px; }
  .back-brand .tagline { font-size: 21px; margin-top: 8px; }
  .movement { font-family: "Oswald", sans-serif; font-size: 18px; color: var(--ink); letter-spacing: .4px; margin-top: 10px; text-transform: uppercase; }

  .intro {
    position: absolute; left: 40px; top: 370px; width: 720px; text-align: center;
    font-family: "Open Sans", sans-serif; font-size: 15.5px; line-height: 20.5px; color: var(--body);
  }

  .contact-bar {
    position: absolute; left: 0; bottom: 0; width: 800px; height: 40px; background: var(--bar);
    display: flex; align-items: center; justify-content: space-between; padding: 0 38px 0 12px;
    font-family: "Open Sans", sans-serif; font-size: 15.5px; color: var(--bar-text); white-space: nowrap;
  }
  .contact-bar__item { display: flex; align-items: center; gap: 10px; }
  .contact-bar svg { width: 12px; height: 12px; fill: var(--gold); flex: none; }
</style>
</head>
<body>
<div class="canvas">

  <section class="card card--front">
    <div class="photo photo--salmon" role="img" aria-label="Plated salmon fillet with asparagus, arugula and cherry tomatoes on a white wooden table"></div>
    <div class="photo photo--lobster" role="img" aria-label="Lobster tail with grilled steak"></div>
    <div class="photo photo--greens" role="img" aria-label="Sautéed greens frittata on a white plate"></div>
    <div class="photo photo--tacos" role="img" aria-label="Soft tacos filled with seasoned meat"></div>

    <div class="brand front-brand">
      <div class="brand__dot"></div>
      <div class="brand__name">Verdant Bayline</div>
      <div class="tagline">Nola made. Nola proud.</div>
    </div>

    <div class="promise">Executive chef quality food right to<br>your door weekly!</div>

    <ol class="steps">
      <li class="step"><span class="step__num">1</span><span class="step__text">Visit Us Online at<br>VerdantBayline.example</span></li>
      <li class="step"><span class="step__num">2</span><span class="step__text">Our Chef Prepares</span></li>
      <li class="step"><span class="step__num">3</span><span class="step__text">We Deliver Right To Your Door</span></li>
    </ol>

    <footer class="contact-bar">
      <span class="contact-bar__item"><svg viewBox="0 0 12 12"><path d="M6 0a4 4 0 0 0-4 4c0 3 4 8 4 8s4-5 4-8a4 4 0 0 0-4-4zm0 5.5A1.5 1.5 0 1 1 6 2.5a1.5 1.5 0 0 1 0 3z"/></svg>418 Marigold avenue, Gretna, Louisiana&nbsp; 70053</span>
      <span class="contact-bar__item"><svg viewBox="0 0 12 12"><path d="M2.5 1l2 2-1 1.5c.7 1.5 1.8 2.6 3.3 3.3L8.3 6.8l2 2-1.3 2C5 10.5 1.5 7 1.2 2.3z"/></svg>(504) 555-0182</span>
      <span class="contact-bar__item"><svg viewBox="0 0 12 12"><circle cx="6" cy="6" r="5.5"/></svg>verdantbayline.example</span>
    </footer>
  </section>

  <section class="card card--back">
    <div class="brand back-brand">
      <div class="brand__dot"></div>
      <div class="brand__name">Verdant Bayline</div>
      <div class="tagline">A new way of eating</div>
      <div class="movement">Join the macrotarian movement today and change your life</div>
    </div>

    <div class="photo photo--bowl" role="img" aria-label="Quinoa salad bowl with green beans, cherry tomatoes, cucumber and feta beside grapes on white marble"></div>

    <p class="intro">To get started, first choose whether you'd like to 'Taste it' with a one-week program a la carte or 'Subscribe' with a subscription that recurs weekly. Our mission is to take care of you through your busy week and help you feel your absolute best, which comes from eating this way as often as possible for your lifestyle.</p>

    <footer class="contact-bar">
      <span class="contact-bar__item"><svg viewBox="0 0 12 12"><path d="M6 0a4 4 0 0 0-4 4c0 3 4 8 4 8s4-5 4-8a4 4 0 0 0-4-4zm0 5.5A1.5 1.5 0 1 1 6 2.5a1.5 1.5 0 0 1 0 3z"/></svg>418 Marigold avenue, Gretna, Louisiana&nbsp; 70053</span>
      <span class="contact-bar__item"><svg viewBox="0 0 12 12"><path d="M2.5 1l2 2-1 1.5c.7 1.5 1.8 2.6 3.3 3.3L8.3 6.8l2 2-1.3 2C5 10.5 1.5 7 1.2 2.3z"/></svg>(504) 555-0182</span>
      <span class="contact-bar__item"><svg viewBox="0 0 12 12"><circle cx="6" cy="6" r="5.5"/></svg>verdantbayline.example</span>
    </footer>
  </section>

</div>
</body>
</html>
```